K.E.L Ventures - Business Card

We need a business card design for a new company based in Malaysia, called K.E.L Ventures Sdn. Bhd. We create, develop & customize database & software/web-based business systems to suit our clients need, mainly in oil&gas industry.

We would like to challenge the creativity of you to design a simple, meaningful, modern, professional & sleek. The design concept may varies but worthy enough for the recipients to proudly keep it in their wallet, and award us with fruitful business opportunities.

B-3-12 Meridan Plaza,
SS21/4, Subang Jaya,
46300 Selangor. Malaysia

http://kelventures-example.com

HAFIZ Roslan | +6012-3817260 | Co-Founder
Di Nazwan | +6012-4092731 | Co-Founder
Abdul Kamil | +6019-5063184 | Managing Director

Target Market(s)

The target market will expand to several other industries such as aviation, communication, automotive, education & hotel.

Industry/Entity Type

Business

Font styles to use
Serif
Sans Serif
Decorative
Script

Requirements
Must have
• plain background yet colourful concept.
Should not have
• something too easy that I can draw myself

```html
<!DOCTYPE html>
<html lang="en">
<head>
<meta charset="utf-8">
<title>K.E.L Ventures – Business Card</title>
<link href="https://fonts.googleapis.com/css2?family=Lato:wght@400;700&display=swap" rel="stylesheet">
<style>
  :root {
    --backdrop: #9b9b9b;
    --card: #1c1c1c;
    --name-pink: #d8345c;
    --role-tan: #a88f6c;
    --phone-green: #77a23a;
    --web-blue: #86c9d8;
    --address-amber: #e9a82a;
    --ink-light: #ffffff;
    --ink-cream: #f3ece0;
    --ink-dark: #1e1a12;
  }
  * { box-sizing: border-box; margin: 0; padding: 0; }
  html, body {
    width: 1200px;
    height: 900px;
    overflow: hidden;
  }
  body {
    background: var(--backdrop);
    font-family: "Lato", sans-serif;
    position: relative;
  }
  .business-card {
    position: absolute;
    left: 100px;
    top: 150px;
    width: 1000px;
    height: 600px;
    background: var(--card);
    border-radius: 40px;
  }
  .label {
    position: absolute;
    white-space: nowrap;
    line-height: 1;
  }
  .person-name {
    left: 120px;
    top: 165px;
    background: var(--name-pink);
    color: var(--ink-light);
    font-size: 56px;
    padding: 10px 22px 12px 20px;
  }
  .person-name .surname { font-weight: 700; }
  .person-role {
    left: 218px;
    top: 243px;
    background: var(--role-tan);
    color: var(--ink-cream);
    font-size: 32px;
    letter-spacing: 1px;
    padding: 10px 26px 10px 24px;
  }
  .contact-phone {
    left: 598px;
    top: 190px;
    background: var(--phone-green);
    color: var(--ink-light);
    font-size: 34px;
    font-weight: 700;
    letter-spacing: 1px;
    padding: 8px 18px 9px 14px;
  }
  .contact-web {
    left: 598px;
    top: 246px;
    background: var(--web-blue);
    color: var(--ink-light);
    font-size: 27px;
    font-weight: 700;
    padding: 9px 16px 9px 14px;
  }
  .company-address {
    left: 62px;
    top: 412px;
    width: 876px;
    background: var(--address-amber);
    color: var(--ink-dark);
    font-size: 27px;
    font-weight: 700;
    padding: 11px 18px 12px 18px;
  }
</style>
</head>
<body>
  <section class="business-card" aria-label="K.E.L Ventures business card">
    <h1 class="label person-name">Di <span class="surname">Nazwan</span></h1>
    <p class="label person-role">CO-FOUNDER</p>
    <p class="label contact-phone">+6012-4092731</p>
    <p class="label contact-web">http://kelventures-example.com</p>
    <address class="label company-address">B-3-12 Meridan Plaza, SS21/4, Subang Jaya, 46300 Selangor. Malaysia</address>
  </section>
</body>
</html>
```